Introductory Flyer

We need a flyer to make businesses aware of our services. We do 3D Printing with a K540 Vantrix Printer(ie make solid prototypes from drawings.

We are a newish company looking to get new business. Photos and text can be taken from our website www.morlenfabworks.com.au and I have permision to use photos from www.vantrix.com if you need any extras. I could also write new text to suit your ideas.

3D Printing is a new technology.  People need to think "Hey! Look what this company can do for us."

Target Market(s)

Anyone designing or needing models of any solid object. Includes engineers, architects, councils, manufacturers. Need to send to businesses and get passed around rather than thrown out.

Industry/Entity Type

Manufacturing

Requirements
Must have
• Something quirky though not too expensive to print. Maybe folded popup card.

• Explain clearly what we actually do. ie 3D Printing and CAD Drawing.

• Not look out of accord with our website www.morlenfabworks.com.au

Nice to have
• Prefer smaller card to A4 sheet. Something to fit in DL envelope. Needs to convey quality and high tech side of our business.

```html
<!DOCTYPE html>
<html lang="en">
<head>
<meta charset="utf-8">
<title>Morlen Fabworks – Ruler Card</title>
<link rel="stylesheet" href="https://fonts.googleapis.com/css2?family=Montserrat:wght@300;600;700&family=Arimo:wght@400&display=swap">
<style>
  :root {
    --backdrop: #f4f2ef;
    --card: #e8e5e5;
    --card-edge: #d3cfcf;
    --tick: #5d5a5a;
    --orange: #f5a44c;
    --quote-soft: #fde3c4;
    --quote-strong: #ffffff;
    --list-ink: #2a2520;
    --brand: #f0962c;
  }
  * { margin: 0; padding: 0; box-sizing: border-box; }
  html, body {
    width: 1200px; height: 724px; overflow: hidden;
    background: var(--backdrop);
  }
  .canvas { position: relative; width: 1200px; height: 724px; }
  .ruler-card {
    position: absolute; left: 50px; top: 101px;
    width: 1100px; height: 522px;
    background: var(--card);
    border: 1px solid var(--card-edge);
    box-shadow: 0 2px 10px rgba(0,0,0,0.12);
  }
  .scale { position: absolute; left: 0; width: 1100px; }
  .scale--cm { top: 0; height: 60px; }
  .scale--inch { bottom: 0; height: 60px; }
  .scale text {
    font-family: "Arimo", sans-serif; font-size: 17px; fill: var(--tick);
  }
  .brand {
    position: absolute; left: 60px; top: 196px;
    display: flex; align-items: center; gap: 12px;
  }
  .brand__mark { width: 30px; height: 30px; background: var(--brand); }
  .brand__name {
    font-family: "Montserrat", sans-serif; font-weight: 700;
    font-size: 25px; line-height: 1.1; color: var(--brand);
  }
  .offer-panel {
    position: absolute; left: 273px; top: 109px;
    width: 827px; height: 309px;
    background: var(--orange);
  }
  .tagline {
    position: absolute; left: 47px; top: 44px;
    font-family: "Montserrat", sans-serif; font-weight: 300;
    font-size: 31px; line-height: 56px; color: var(--quote-soft);
  }
  .tagline strong { font-weight: 600; color: var(--quote-strong); }
  .services {
    position: absolute; left: 393px; top: 50px;
    font-family: "Arimo", sans-serif; font-size: 21px;
    line-height: 35px; color: var(--list-ink); list-style: none;
  }
  .services__web { margin-top: 35px; }
</style>
</head>
<body>
<div class="canvas">
  <div class="ruler-card">
    <svg class="scale scale--cm" viewBox="0 0 1100 60" aria-hidden="true">
      <defs>
        <pattern id="mm" x="26" y="0" width="5.25" height="60" patternUnits="userSpaceOnUse">
          <line x1="0.5" y1="0" x2="0.5" y2="9" stroke="#5d5a5a" stroke-width="1"/>
        </pattern>
        <pattern id="halfcm" x="26" y="0" width="26.25" height="60" patternUnits="userSpaceOnUse">
          <line x1="0.5" y1="0" x2="0.5" y2="14" stroke="#5d5a5a" stroke-width="1"/>
        </pattern>
        <pattern id="cm" x="26" y="0" width="52.5" height="60" patternUnits="userSpaceOnUse">
          <line x1="0.5" y1="0" x2="0.5" y2="20" stroke="#5d5a5a" stroke-width="1.2"/>
        </pattern>
      </defs>
      <rect x="26" y="0" width="1051" height="60" fill="url(#mm)"/>
      <rect x="26" y="0" width="1051" height="60" fill="url(#halfcm)"/>
      <rect x="26" y="0" width="1051" height="60" fill="url(#cm)"/>
      <g text-anchor="middle">
        <text x="26" y="42">0</text><text x="131" y="42">2</text><text x="236" y="42">4</text>
        <text x="341" y="42">6</text><text x="446" y="42">8</text><text x="551" y="42">10</text>
        <text x="656" y="42">12</text><text x="761" y="42">14</text><text x="866" y="42">16</text>
        <text x="971" y="42">18</text><text x="1076" y="42">20</text>
      </g>
    </svg>

    <div class="brand">
      <span class="brand__mark"></span>
      <span class="brand__name">Morlen<br>Fabworks</span>
    </div>

    <div class="offer-panel">
      <p class="tagline">“communicate<br>your <strong>ideas</strong><br><strong>in 3D</strong> quickly<br>and easily”</p>
      <ul class="services">
        <li>Offering 3D modeling solutions:</li>
        <li>- Rapid Prototyping</li>
        <li>- CAD Drawing</li>
        <li>- 3D Printing</li>
        <li class="services__web">http://www.morlenfabworks.com.au</li>
      </ul>
    </div>

    <svg class="scale scale--inch" viewBox="0 0 1100 60" aria-hidden="true">
      <defs>
        <pattern id="eighth" x="19" y="0" width="16.625" height="60" patternUnits="userSpaceOnUse">
          <line x1="0.5" y1="51" x2="0.5" y2="60" stroke="#5d5a5a" stroke-width="1"/>
        </pattern>
        <pattern id="halfinch" x="19" y="0" width="66.5" height="60" patternUnits="userSpaceOnUse">
          <line x1="0.5" y1="46" x2="0.5" y2="60" stroke="#5d5a5a" stroke-width="1"/>
        </pattern>
        <pattern id="inch" x="19" y="0" width="133" height="60" patternUnits="userSpaceOnUse">
          <line x1="0.5" y1="40" x2="0.5" y2="60" stroke="#5d5a5a" stroke-width="1.2"/>
        </pattern>
      </defs>
      <rect x="19" y="0" width="1066" height="60" fill="url(#eighth)"/>
      <rect x="19" y="0" width="1066" height="60" fill="url(#halfinch)"/>
      <rect x="19" y="0" width="1066" height="60" fill="url(#inch)"/>
      <g text-anchor="middle">
        <text transform="translate(19 22) rotate(180)">8</text>
        <text transform="translate(152 22) rotate(180)">7</text>
        <text transform="translate(285 22) rotate(180)">6</text>
        <text transform="translate(418 22) rotate(180)">5</text>
        <text transform="translate(551 22) rotate(180)">4</text>
        <text transform="translate(684 22) rotate(180)">3</text>
        <text transform="translate(817 22) rotate(180)">2</text>
        <text transform="translate(950 22) rotate(180)">1</text>
        <text transform="translate(1083 22) rotate(180)">0</text>
      </g>
    </svg>
  </div>
</div>
</body>
</html>
```